Paint Retail Store needs a logo/label redesign.

We are redesigning a label for one of our products. We are a paint retail store that specializes on selling premium paint at outlet prices called Brush & Gleam. We want the redesign to exude professionalism and cleanliness. Attached is a picture of our current label. We want the logo Brush & Gleam to be modified to a more modern feel that still incorporates the iconic paint roller element that has been part of our brand identity. We want the description of: Exceptional Durability/ Luxurious Finish to be included in the front of the label to attract our clients. Include all of the information and description of the current label to the new label. Attached are pictures of our competitors labels so you have an idea of what we are looking for. We also want the background of the label to be a clean solid color.

Target Market(s)

Home Owners, DIY enthusiasts, Contractors/painters, interior designers

Industry/Entity Type

Paint and Coatings retail store

Colors

Designer to choose colors to be used in the design.

Requirements
Must have
• Semigloss Finish, Exceptional Durability, Luxurios Finish. Include all the information that are on the side of the current label to the new label. Include the phrase: Made in the US.
Nice to have
• A redesign of the logo: Brush & Gleam to convey a more modern/professional look.
Should not have
• Feminine colors.

```html
<!DOCTYPE html>
<html lang="en">
<head>
<meta charset="utf-8">
<title>Brush &amp; Gleam Semi-Gloss Latex Paint Label</title>
<link href="https://fonts.googleapis.com/css2?family=Montserrat:wght@700;800&family=Roboto+Condensed:wght@400;500&family=Open+Sans:wght@400&family=Cinzel:wght@400&family=Saira+Condensed:wght@300&family=Lobster&display=swap" rel="stylesheet">
<style>
  :root{
    --blue-deep:#0b3f86;
    --blue-mid:#0f63b0;
    --blue-light:#1d8fd6;
    --navy:#0d2747;
    --panel:#123c74;
    --orange:#ef8a24;
    --gold:#c9992f;
    --white:#ffffff;
    --grey:#8f9399;
    --ice:#4fb3e8;
  }
  *{margin:0;padding:0;box-sizing:border-box}
  html,body{width:1200px;height:872px;overflow:hidden;background:#fff}
  .label{
    position:relative;width:1200px;height:872px;overflow:hidden;
    background:radial-gradient(ellipse at 50% 35%,var(--blue-light) 0%,var(--blue-mid) 40%,var(--blue-deep) 100%);
    color:var(--white);
    font-family:"Roboto Condensed",sans-serif;
  }
  .copy{position:absolute;width:282px;font-size:11.6px;line-height:14.45px;text-align:justify}
  .copy-left{left:51px;top:64px;font-weight:500}
  .copy-right{left:863px;top:64px;font-weight:400}
  .copy p{margin:0}
  .gap{margin-top:14.45px!important}
  .alert{color:var(--orange);font-weight:500}
  .ingredients{
    position:absolute;left:65px;top:655px;width:256px;height:173px;
    background:var(--navy);border-radius:10px;padding:12px 24px;
    font-size:11.8px;line-height:14.45px;
  }
  .ingredients h3{
    font-family:"Open Sans",sans-serif;font-weight:400;font-size:16px;
    display:flex;gap:20px;border-bottom:2px solid var(--white);padding-bottom:4px;margin-bottom:12px;
  }
  .ingredients .row{display:flex;white-space:nowrap}
  .ingredients .dots{flex:1;border-bottom:1px dotted var(--white);margin:0 1px 4px}
  .ingredients .note{margin-top:14px}
  .finish{
    position:absolute;left:456px;top:28px;width:288px;height:56px;
    background:var(--orange);border-top:8px solid var(--grey);
    font-family:"Montserrat",sans-serif;font-weight:800;font-size:29px;
    display:flex;align-items:center;justify-content:center;letter-spacing:1px;
  }
  .brand{position:absolute;left:460px;top:170px;width:290px;display:flex;align-items:center;justify-content:center;gap:14px}
  .brand-dot{width:40px;height:40px;border-radius:50%;background:var(--orange);flex:none}
  .brand-name{font-family:"Montserrat",sans-serif;font-weight:800;font-size:48px;line-height:50px;color:var(--white)}
  .tagline{position:absolute;left:440px;top:336px;width:320px;text-align:center;font-family:"Saira Condensed",sans-serif;font-weight:300;font-size:24px}
  .crown{position:absolute;left:588px;top:398px;width:24px;height:16px;background:var(--gold)}
  .rule{position:absolute;height:1px;background:var(--gold)}
  .grade{position:absolute;left:470px;top:416px;width:260px;text-align:center;font-family:"Cinzel",serif;font-size:28px;color:var(--gold);line-height:34px}
  .claim{position:absolute;width:400px;left:400px;text-align:center;font-family:"Open Sans",sans-serif;font-size:27px;line-height:34px}
  .product{position:absolute;left:420px;top:548px;width:360px;text-align:center;font-family:"Lobster",cursive;font-size:70px;color:var(--orange);line-height:80px}
  .use{
    position:absolute;left:420px;top:633px;width:348px;height:55px;background:var(--grey);
    font-family:"Montserrat",sans-serif;font-weight:700;font-size:26px;
    display:flex;align-items:center;justify-content:center;
  }
  .badge{position:absolute;left:549px;top:707px;width:86px;height:86px;border-radius:50%;background:var(--ice)}
  .volume{position:absolute;left:440px;top:806px;width:320px;text-align:center;font-family:"Saira Condensed",sans-serif;font-weight:300;font-size:22px}
  .origin{position:absolute;left:339px;top:816px;font-family:"Saira Condensed",sans-serif;font-weight:300;font-size:14px}
  .steps{position:absolute;left:863px;top:156px;width:282px;height:177px;background:var(--panel)}
  .steps-title{
    position:absolute;left:31px;top:-5px;width:219px;height:18px;background:var(--orange);
    font-size:11.5px;font-weight:500;display:flex;align-items:center;justify-content:center;
  }
  .step-grid{position:absolute;left:16px;top:17px;right:12px;display:grid;grid-template-columns:repeat(3,1fr);row-gap:8px}
  .step{font-size:7px;line-height:9px}
  .step-icon{width:49px;height:49px;background:#111;border:2px solid var(--white);margin-bottom:4px}
  .step-divider{position:absolute;left:16px;right:12px;top:92px;height:1px;background:var(--white);opacity:.7}
</style>
</head>
<body>
<main class="label">

  <section class="copy copy-left">
    <p>Where To Use: Walls cabinets, cellings, trim and doors. Use over drywall, wood, concrete/brick plaster and wallpaper. See bellow for preparation steps:</p>
    <p>How Much You Need: For one coat coverage, apply at a maximum of 400 square feet per gallon. Rough or textured surfaces may require more allow for 125-300 square feet per gallon. Do not thin.</p>
    <p>What Tools To Use: May be applied with a quality roller, a nylon/polyester brush, or a paint pad How To Apply Room and surface temperature must be 50 degrees Fahrenheit. Allow at least 4 hours of drying time before recoating. Mix gallons toghether for color and sheen uniformity when using more than one gallon of the same product</p>
    <p>Care for Freshly Painted Surfaces. Freshly painted surfaced may be washed either 30 days- Until then avoid touching, wiping, or wetting the surface. Then clean with mild, non-abrasive, non-oily cleanser and water. Do not place objects on painted sirfaces untill throughly dry. Soap and Water Cleanup</p>
    <p>HOW TO PREPARE THE SURFACE</p>
    <p>Previously Painted Surfaces: Remove loose paint, Wash with a mild, non-abrasive, non-oily cleanser and water. Rinse completely, let dry Patch holes and cracks with speckling paste and let dry. Sand patched area and wipe off residue. Send all smooth or glossy surfaces, nnse well. Unpainted Surfaces: Wallboard or brywall Concrete/brick Allow new masonry to sure at least 30 days Etch smooth unpainted concrete. Remove all loose concrete and efflorescence: Rinse and allow to dry Plaster (new) Must be died and cured for 30 days. Prime with primer. Let dry 4 hours before top coating. Wallpaper Vinyl coated wallpaper may be coated if all seams and edges are glued tight, Self-sand and wipe clean. Use primer and alllow 24 hours to dry.</p>
  </section>

  <section class="ingredients">
    <h3><span>CAS NO.</span><span>INGREDIENTS</span></h3>
    <div class="row"><span>7732-18-5</span><span class="dots"></span><span>Water</span></div>
    <div class="row"><span>Propietary</span><span class="dots"></span><span>Vinyl Polymer</span></div>
    <div class="row"><span>&nbsp;13463-67-7</span><span class="dots"></span><span>Titanium Dioxide</span></div>
    <div class="row"><span>Proprietary</span><span class="dots"></span><span>Acrylic Polymer</span></div>
    <div class="row"><span>471-34-1</span><span class="dots"></span><span>Calcium Carbonate</span></div>
    <div class="row"><span>14464-46-1</span><span class="dots"></span><span>Cristobalite</span></div>
    <p class="note">NON-PHOTOCHEMICALLY REACTIVE</p>
  </section>

  <div class="finish">SEMI - GLOSS</div>

  <div class="brand">
    <span class="brand-dot"></span>
    <span class="brand-name">Brush &amp;<br>Gleam</span>
  </div>
  <p class="tagline">Premium Paint at Outlet Prices</p>

  <div class="crown" role="img" aria-label="Small gold crown ornament"></div>
  <div class="rule" style="left:483px;top:416px;width:234px"></div>
  <p class="grade">PREMIUM GRADE</p>
  <div class="rule" style="left:483px;top:450px;width:234px"></div>
  <p class="claim" style="top:454px">EXCEPTIONAL DURABILITY</p>
  <div class="rule" style="left:483px;top:490px;width:234px;background:var(--gold)"></div>
  <p class="claim" style="top:493px">LUXURIOUS FINISH</p>

  <p class="product">Latex Paint</p>
  <div class="use">INTERIOR / EXTERIOR</div>

  <div class="badge" role="img" aria-label="Frozen product badge"></div>

  <p class="origin">Made in the US.</p>
  <p class="volume">1 Gal. (124 OZ/3.667 Lts.)</p>

  <section class="copy copy-right">
    <p class="alert">SOLID VINYL WALLPAPER CANNOT BE PAINTED</p>
    <p class="gap">CAUTIONS CONTAINS CRYSTALLINE SILICA- Use Cleanup: Clean tools, spills and splatters immediately with soap and water.</p>
    <div style="height:200px"></div>
    <p>only with adecuate ventilation To avoid overexposure, open windows and doors or use other means to ensure fresh air entry during aplication and drying. If you experience eye watering, headaches, or dizzyness, increase fresh air, or wear respiratory protection or leave the area. Adecuate ventilation required when sending or abrading the dried film. If adequate ventilation cannot ve provided wear an approved particulate respirator. Follow resporator manufacturer's directions for respirator use. Avoid contact with eyes and skin Wash hands after using. Keep container closed when not in use Do not transfer contents to other containers for storage</p>
    <p class="gap">FIRST AID. In case of eye contact flush thoroughly with large amounts of water. Get medical attention if mation persists, fallowed, call Poison Control Center. hospital emergency room, or physician immediately</p>
    <p class="gap">DELAYED EFFECTS FROM LONG TERM OVEREXPOSURE Abrading on sanding of the dry film may release crystalino silica which has been shown to cause lung damage and cancer under long term expusurur</p>
    <p class="gap">WARNING: This product contains chemicals known to the State of California to cause cancer and birth defects or other reproductive ha</p>
    <p class="gap">DO NOT TAKE INTERNALLY<br>KEEP OUT OF THE REACH OF CHILDREN</p>
  </section>

  <section class="steps">
    <div class="steps-title">KEEP FROM FREEZING-DO NOT THIN</div>
    <div class="step-divider"></div>
    <div class="step-grid">
      <div class="step"><div class="step-icon" role="img" aria-label="Pictogram of a hand wiping a surface"></div>Clean, dull and<br>dry surface</div>
      <div class="step"><div class="step-icon" role="img" aria-label="Pictogram of paint being stirred"></div>Stir paint<br>thoroughly</div>
      <div class="step"><div class="step-icon" role="img" aria-label="Pictogram of a brush at the ceiling edge"></div>Start at<br>ceiling edge</div>
      <div class="step"><div class="step-icon" role="img" aria-label="Pictogram of a roller painting an N pattern"></div>Paint "N"<br>pattern-fill in</div>
      <div class="step"><div class="step-icon" role="img" aria-label="Pictogram of a brush painting trim"></div>Paint trim last</div>
      <div class="step"><div class="step-icon" role="img" aria-label="Pictogram of tools rinsed under water"></div>Soap and<br>water clean up</div>
    </div>
  </section>

</main>
</body>
</html>
```